Classic/Royal 5 Items Black coloured Stationery Design

Hello,
I'm looking for an Elegant Stationery set consists of 5 items as the following,
1- Letterhead
2- Business Card
3- Invoice
4- CD/DVD with their Envelope Design
5- Envelope
To let the project move ahead easily, I've included a folder consists many designs I liked from various design sites and it consists of,
1- Business card
2- Corporate Identity
3- Invoice
4- Miscellanies
Inside the first three folders, you will find a folder named "Recommended", it contains designs that I like so much and hoping to have a design like them.
The "Miscellanies" folder got some designs for Inspiration.
I'm waiting for some greats designs, a joomla template designer is a bonus for me as I will need him to design the website layer soon.
Due to upload problems at ArtHerdly, I've uploaded the folder in a .rar archive at multiple site and here is the link http://zup.qx/TRALVBNE .
Thank you
Update :- You can use this alternative download link from my Google drive to download the designs
https://files.plomwex.net/file/d/7Kq2ZpR4m8sVxT1nLw9cYb3HfJd5

```html
<!DOCTYPE html>
<html lang="en">
<head>
<meta charset="utf-8">
<title>Velvane Letterhead</title>
<link href="https://fonts.googleapis.com/css2?family=Oswald:wght@400;500&family=Montserrat:wght@400&display=swap" rel="stylesheet">
<style>
  :root {
    --ink: #000000;
    --royal-blue: #5169af;
    --paper: #ffffff;
    --text-grey: #585858;
    --logo-grey: #bdbdbd;
  }
  html, body {
    margin: 0;
    padding: 0;
    overflow: hidden;
    background: var(--paper);
  }
  .letterhead {
    position: relative;
    width: 849px;
    height: 1200px;
    background: var(--paper);
    overflow: hidden;
  }
  .contact-block {
    position: absolute;
    left: 21px;
    top: 22px;
    font-family: "Oswald", sans-serif;
    font-weight: 500;
    font-size: 19px;
    line-height: 25.7px;
    letter-spacing: 1.9px;
    color: var(--text-grey);
  }
  .contact-row {
    display: flex;
    white-space: nowrap;
  }
  .contact-label { width: 80px; }
  .contact-colon { width: 23px; }
  .header-accent {
    position: absolute;
    left: 589px;
    top: 0;
    width: 20px;
    height: 171px;
    background: var(--royal-blue);
  }
  .brand-panel {
    position: absolute;
    left: 609px;
    top: 0;
    width: 240px;
    height: 171px;
    background: var(--ink);
    display: flex;
    flex-direction: column;
    align-items: center;
    justify-content: center;
    color: var(--logo-grey);
  }
  .brand-mark {
    width: 38px;
    height: 46px;
    border: 2px solid var(--logo-grey);
    box-sizing: border-box;
    margin-bottom: 6px;
  }
  .brand-name {
    font-family: "Oswald", sans-serif;
    font-weight: 400;
    font-size: 21px;
    line-height: 1;
    letter-spacing: 0.5px;
  }
  .brand-tagline {
    font-family: "Montserrat", sans-serif;
    font-size: 8px;
    margin-top: 4px;
    white-space: nowrap;
  }
  .band {
    position: absolute;
    left: 0;
    width: 849px;
    height: 41px;
    display: flex;
  }
  .band--top { top: 171px; }
  .band--bottom { top: 1159px; }
  .band-black { width: 424px; background: var(--ink); }
  .band-blue { flex: 1; background: var(--royal-blue); }
</style>
</head>
<body>
  <div class="letterhead">
    <div class="contact-block">
      <div class="contact-row">12345 Larkfield Stone Road</div>
      <div class="contact-row"><span class="contact-label">Mobile</span><span class="contact-colon">:</span><span>5550147823</span></div>
      <div class="contact-row"><span class="contact-label">Fax</span><span class="contact-colon">:</span><span>48172</span></div>
      <div class="contact-row"><span class="contact-label">e-mail</span><span class="contact-colon">:</span><span>email@velvane.com</span></div>
      <div class="contact-row"><span class="contact-label">Website</span><span class="contact-colon">:</span><span>www.velvane.com</span></div>
    </div>

    <div class="header-accent"></div>
    <div class="brand-panel">
      <div class="brand-mark"></div>
      <div class="brand-name">Velvane</div>
      <div class="brand-tagline">Resorts and Trade Provisions</div>
    </div>

    <div class="band band--top"><div class="band-black"></div><div class="band-blue"></div></div>
    <div class="band band--bottom"><div class="band-black"></div><div class="band-blue"></div></div>
  </div>
</body>
</html>
```